Modeboutique Eröffnungs-Flyer
Zielgruppe
Die Lerch Textil AG ist ein seit über 20 Jahren bestehende Boutique und besteht heute noch aus einer Filiale im Wiesenhof-Center Gränichen. Der Betrieb wird von hier aus geleitet und ist auch im Familienbesitz. Zielgruppe sind Herren und Damen ab 30, regionale Einkäufer.
Aufgabenstellung
Folgendes:
Am 26./27./28. März 2015 veranstalten wir einen Frühlings-Modeapéro.
- Rabatt 10%
- Vorstellung neuer Kollektionen
- Beratung
- Getränke, Cüpli, Weisswein, Säfte etc.
- Apéro-Häppchen
Dieser Anlass soll folgendermassen bekannt gemacht werden:
- Persönliche Einladung an Stammkunden (Flyer mit aufgedruckter Adresse des Kunden) A5, quer 4-seitig. (siehe Bestimmung für Postsendungen bei den Links)
Vorderseite: Übersicht über die Angebote
Rückseite: Adresse Empfänger
Innenseite links: Thema des neuen Ladenlooks
Innenseite rechts: Einladung zum Aper mit den Angeboten und einen Gutschein zum mitbringen.
Wichtig: Wir haben im Januar unseren Laden renoviert und dieser Anlass soll zugleich unter dem Motto „offizielle Einweihung des neuen Ladenlooks“ laufen. Also irgendwie auf Begleitschreiben, Inserat und Plakat mit dem Apéro in Verbindung bringen.
Können Sie ein optisch attraktives Layout für die Druckdateien entwerfen? Soll im Briefkasten irgendwie auffallen und eben nicht einfach im Eimer landen ;-).
Der Web-Auftritt www.lerchtextil.ch zeigt Ihnen noch gewisse Eindrücke, ist aber sehr bescheiden, da wir dort mit einer Filiale nicht weiter investieren werden. Wir haben auch noch kein einheitliches Grafikkonzept oder so etwas, was wir auch nicht wollen. Der Flyer sollte aber die Basis zu Nur das Logo, das seit 20 Jahren besteht aktuell aber noch redesignt wird, es wird aber ähnlich daherkommen. Die Aktionen sollen zweckmässig sein und nicht teurer Perfektionismus aber im Laufe der Renovierung soll auch ein Hauch von professioneller Werbung einfliessen.
Bilder können Sie von der Website als Platzhalterbilder verwenden – sind aber noch das alte Ladenlokal. Da werden wir nach Bestimmung des Gewinnerdesigns die Hochaufgelösten Daten zustellen.

```html
<!DOCTYPE html>
<html lang="de">
<head>
<meta charset="utf-8">
<title>Lerch Textil – Einladung Frühlings-Modeapéro</title>
<link rel="stylesheet" href="https://fonts.googleapis.com/css2?family=Montserrat:wght@200;300;400;500;600;700;800&family=Open+Sans:wght@400;600;700&display=swap">
<style>
  :root{
    --pink:#dc2a55;
    --pink-dark:#c01f47;
    --ink:#111111;
    --text:#2a2a2a;
    --stage-light:#f4f4f4;
    --stage-dark:#dcdcdc;
    --white:#ffffff;
    --muted:#7a7a7a;
  }
  *{margin:0;padding:0;box-sizing:border-box}
  html,body{width:1200px;height:1200px;overflow:hidden}
  body{
    position:relative;
    background:radial-gradient(ellipse at 50% 45%,var(--stage-light) 0%,var(--stage-light) 40%,var(--stage-dark) 100%);
    font-family:"Open Sans",Arial,sans-serif;
    color:var(--text);
  }
  .side-label{position:absolute;left:0;width:1200px;text-align:center;font-size:14px;color:var(--muted)}
  .side-label--outer{top:78px}
  .side-label--inner{top:634px}

  .spread{position:absolute;left:25px;width:1151px;height:406px;overflow:hidden;background:var(--white)}
  .spread--outer{top:112px}
  .spread--inner{top:670px;background:linear-gradient(180deg,#f3f4f6 0%,#e9ecef 100%)}

  /* outer spread */
  .map-area{position:absolute;left:0;top:0}
  .stamp-box{position:absolute;left:411px;top:20px;width:146px;height:75px;border:1px solid #bfbfbf;background:var(--white)}
  .recipient{position:absolute;left:382px;top:243px;font-size:9.5px;line-height:12.6px;color:var(--ink);font-style:normal}
  .info-block{position:absolute;top:298px}
  .info-block--contact{left:20px}
  .info-block--hours{left:182px}
  .info-title{font-family:"Montserrat",sans-serif;font-weight:600;font-size:13px;color:var(--ink);margin-bottom:4px;letter-spacing:-.2px}
  .info-line{font-size:7.4px;line-height:9.4px;color:var(--ink)}
  .info-line--accent{color:var(--pink);font-weight:700}
  .info-gap{height:9.5px}
  .info-web{color:var(--pink)}
  .outer-band{position:absolute;left:0;bottom:0;width:1151px;height:21px;background:var(--pink)}

  .cover{position:absolute;left:576px;top:0;width:575px;height:385px;background:linear-gradient(135deg,#f6f7f9 0%,#e6e9ed 100%);overflow:hidden}
  .cover-date{position:absolute;left:24px;top:22px;font-family:"Montserrat",sans-serif;font-weight:700;font-size:18.5px;letter-spacing:-.6px;color:var(--pink)}
  .cover-date span{color:var(--ink)}
  .cover-title{position:absolute;left:22px;top:38px;font-family:"Montserrat",sans-serif;font-weight:800;font-size:58px;letter-spacing:-3.4px;line-height:1;color:var(--ink)}
  .cover-sub{position:absolute;left:24px;top:92px;font-family:"Montserrat",sans-serif;font-weight:300;font-size:20.5px;letter-spacing:-.5px;color:var(--ink)}
  .cover-photo{position:absolute;left:306px;top:0;width:269px;height:385px;background:linear-gradient(160deg,#d6b08a 0%,#c49068 35%,#efe4dc 70%,#e9e6e3 100%)}
  .offer-banner{position:absolute;left:0;top:156px}
  .offer-list{position:absolute;left:39px;top:166px;list-style:none;font-family:"Montserrat",sans-serif;font-weight:500;font-size:12.4px;line-height:19px;color:var(--white);letter-spacing:-.2px}
  .brand-name{font-family:"Montserrat",sans-serif;font-weight:700;color:var(--ink);letter-spacing:-.8px;line-height:1;white-space:nowrap}
  .brand-name--cover{position:absolute;left:30px;top:328px;font-size:30px}

  /* inner spread */
  .look-title{position:absolute;left:24px;top:20px;font-family:"Montserrat",sans-serif;font-size:62px;line-height:1;letter-spacing:-3px;white-space:nowrap;z-index:3}
  .look-title .w-im{font-weight:200;color:var(--ink)}
  .look-title .w-neuen{font-weight:200;color:var(--pink)}
  .look-title .w-look{font-weight:800;color:var(--pink);-webkit-text-stroke:3px var(--white);paint-order:stroke fill}
  .look-copy{position:absolute;left:25px;top:92px;width:240px;font-size:8.2px;line-height:10.4px;color:#333;z-index:2}
  .look-copy p+p{margin-top:10px}
  .team-photo{position:absolute;left:19px;top:187px;width:335px;height:219px;background:linear-gradient(180deg,rgba(230,232,235,0) 0%,#cdb9ad 25%,#8a6e66 55%,#3f3a3c 100%);border-radius:40px 40px 0 0;z-index:2}
  .collage{position:absolute;left:0;top:0;z-index:1}
  .specials-title{position:absolute;right:13px;top:28px;font-family:"Montserrat",sans-serif;font-weight:200;font-size:58px;letter-spacing:-3px;color:var(--pink);line-height:1}
  .specials-list{position:absolute;right:17px;top:114px;list-style:none;text-align:right;font-family:"Montserrat",sans-serif;font-weight:600;font-size:13.6px;line-height:25px;letter-spacing:-.6px;color:var(--ink)}
  .brand-name--voucher{position:absolute;left:896px;top:272px;font-size:18px;letter-spacing:-.6px}
  .voucher-percent{position:absolute;right:12px;top:247px;font-family:"Montserrat",sans-serif;font-weight:200;font-size:78px;letter-spacing:-4px;line-height:1;color:var(--pink)}
  .voucher-rabat{position:absolute;right:10px;top:318px;font-family:"Montserrat",sans-serif;font-weight:800;font-size:76px;letter-spacing:-5px;line-height:1;color:var(--pink)}
</style>
</head>
<body>

<div class="side-label side-label--outer">Außenseite</div>

<section class="spread spread--outer">
  <svg class="map-area" width="360" height="280" viewBox="0 0 360 280">
    <path d="M0 0 H300 C330 70 345 170 328 279 H0 Z" fill="#e8e5de" role="img" aria-label="Stadtplan mit Lage der Boutique"/>
    <path d="M300 0 C333 70 350 170 332 279" fill="none" stroke="var(--pink)" stroke-width="5"/>
  </svg>

  <div class="stamp-box"></div>

  <address class="recipient">
    Ditta<br>z.H. Peter Beispiel<br>Rue de l’Exemple 66<br>P.O. Box<br>1234 Musterstadt
  </address>

  <div class="info-block info-block--contact">
    <h3 class="info-title">Kontakt</h3>
    <p class="info-line info-line--accent">Lerch Textil AG</p>
    <p class="info-line">Wiesenweg 7 - 5722 Gränichen</p>
    <div class="info-gap"></div>
    <p class="info-line">Fon. 062 000 41 18</p>
    <div class="info-gap"></div>
    <p class="info-line info-web">www.lerchtextil.ch - info@lerchtextil.ch</p>
  </div>

  <div class="info-block info-block--hours">
    <h3 class="info-title">Öffnungszeiten</h3>
    <p class="info-line info-line--accent">Montag - Freitag</p>
    <p class="info-line">8.30-12.00 Uhr - 13.30-19:00 Uhr</p>
    <div class="info-gap"></div>
    <p class="info-line info-line--accent">Samstag</p>
    <p class="info-line">8.00-16.00 Uhr</p>
  </div>

  <div class="cover">
    <div class="cover-photo" role="img" aria-label="Fotomodell mit langen blonden Locken im weissen Oberteil"></div>
    <p class="cover-date">26./27./28. <span>MÄRZ</span> 2015</p>
    <h1 class="cover-title">EINLANDUNG</h1>
    <p class="cover-sub">zum Frühlings-Modeapéro</p>
    <svg class="offer-banner" width="345" height="113" viewBox="0 0 345 113">
      <polygon points="0,0 345,0 308,112 0,112" fill="var(--pink)"/>
      <line x1="0" y1="0.5" x2="345" y2="0.5" stroke="var(--pink-dark)" stroke-width="1"/>
    </svg>
    <ul class="offer-list">
      <li>Rabatt 10%</li>
      <li>Vorstellung neuer Kollektionen</li>
      <li>Beratung</li>
      <li>Getränke, Cüpli, Weisswein, Säfte etc.</li>
      <li>Apéro-Häppchen</li>
    </ul>
    <p class="brand-name brand-name--cover">Lerch Textil</p>
  </div>

  <div class="outer-band"></div>
</section>

<div class="side-label side-label--inner">Innenseite</div>

<section class="spread spread--inner">
  <svg class="collage" width="1151" height="406" viewBox="0 0 1151 406">
    <defs>
      <clipPath id="collage-shape">
        <ellipse cx="578" cy="203" rx="305" ry="381"/>
      </clipPath>
    </defs>
    <g clip-path="url(#collage-shape)">
      <rect x="270" y="0" width="620" height="406" fill="var(--pink)"/>
      <rect x="270" y="0" width="303" height="201" fill="#b79a78" role="img" aria-label="Verkaufsraum mit Holzboden und farbigen Shirts"/>
      <rect x="577" y="0" width="310" height="201" fill="#8f8a72" role="img" aria-label="Regale mit gefalteten Jeans und Jacken"/>
      <rect x="270" y="206" width="331" height="174" fill="#9c9580" role="img" aria-label="Ladeninneres mit Kleiderständern"/>
      <rect x="605" y="206" width="285" height="174" fill="#7f8580" role="img" aria-label="Schaufenster des Velora-Stores"/>
      <rect x="270" y="381" width="620" height="25" fill="var(--pink)"/>
      <text x="338" y="398" font-family="Open Sans, sans-serif" font-size="10" fill="#ffffff">www.lerchtextil.ch  -  www.lerchtextil.ch  -  www.lerchtextil.ch  -  www.lerchtextil.ch  -  www.lerchtextil.ch</text>
    </g>
    <ellipse cx="578" cy="203" rx="305" ry="381" fill="none" stroke="var(--pink)" stroke-width="3"/>
    <ellipse cx="578" cy="203" rx="314" ry="388" fill="none" stroke="#9a9a9a" stroke-width="1" stroke-dasharray="2 3"/>
  </svg>

  <h2 class="look-title"><span class="w-im">IM</span> <span class="w-neuen">NEUEN</span> <span class="w-look">LOOK</span></h2>

  <div class="look-copy">
    <p>Sportliche, modische und zugleich elegante Mode erwartet die Besucherinnen bei Lerch Textil in Gränichen. Auch die Herren kommen auf ihre Kosten. Und im Velora-Store findet man eine ansprechende Auswahl für sie und ihn.</p>
    <p>Wir freuen uns ab Dienstag 3. Februar 2015 in neuem Look wieder für Sie da zu sein und stossen mit Ihnen gerne auf die neue Ladenausgestaltung an.</p>
  </div>

  <div class="team-photo" role="img" aria-label="Vier Mitarbeiterinnen stossen mit Sektgläsern an"></div>

  <h2 class="specials-title">SPECIALS</h2>
  <ul class="specials-list">
    <li>Vorstellung neuer Kollektionen</li>
    <li>Beratung</li>
    <li>Getränke, Cüpli, Weisswein, Säfte etc.</li>
    <li>Apéro-Häppchen</li>
  </ul>

  <p class="brand-name brand-name--voucher">Lerch Textil</p>
  <p class="voucher-percent">10%</p>
  <p class="voucher-rabat">RABAT</p>
</section>

</body>
</html>
```